Kiteloft Namecard

We have a regular but rotating group of Actors and Directors who meet weekly. I'd like to make a nametag (first and last names) for each of the participants which would fit on a regular business card. The first name would be over-sized to enable reading at a distance. The background & border should project fun and warmth. The Kiteloft is meant to be a place to play without judgement or negative vibes.

```html
<!DOCTYPE html>
<html lang="en">
<head>
<meta charset="utf-8">
<title>Kiteloft Namecard – Nora Kessler</title>
<link rel="stylesheet" href="https://fonts.googleapis.com/css2?family=Abril+Fatface&family=Raleway:wght@500&family=Libre+Baskerville:wght@700&display=swap">
<style>
  :root {
    --sky-top: #2fa9d8;
    --sky-mid: #8fc9d6;
    --haze: #e8d6a0;
    --sea: #cfc3a0;
    --sand-light: #e6c98a;
    --sand: #d8b06a;
    --sand-deep: #c99a55;
    --ink-white: #ffffff;
    --shadow: rgba(40, 30, 10, 0.55);
  }

  html, body {
    margin: 0;
    padding: 0;
    width: 1200px;
    height: 686px;
    overflow: hidden;
    background: #ffffff;
  }

  .namecard {
    position: relative;
    width: 1200px;
    height: 686px;
    overflow: hidden;
  }

  .beach-photo {
    position: absolute;
    inset: 0;
    background:
      linear-gradient(180deg,
        var(--sky-top) 0%,
        var(--sky-mid) 22%,
        var(--haze) 42%,
        var(--sea) 50%,
        var(--sand-light) 58%,
        var(--sand) 78%,
        var(--sand-deep) 100%);
  }

  .first-name {
    position: absolute;
    left: 7px;
    width: 1200px;
    top: -52px;
    margin: 0;
    text-align: center;
    font-family: "Abril Fatface", serif;
    font-weight: 400;
    font-size: 360px;
    line-height: 1;
    letter-spacing: -6px;
    color: var(--ink-white);
    text-shadow: 6px 8px 10px var(--shadow);
  }

  .last-name {
    position: absolute;
    left: 22px;
    width: 1200px;
    top: 344px;
    margin: 0;
    text-align: center;
    font-family: "Raleway", sans-serif;
    font-weight: 500;
    font-size: 52px;
    line-height: 1;
    letter-spacing: 0.82em;
    text-indent: 0.82em;
    color: var(--ink-white);
    text-shadow: 3px 4px 5px var(--shadow);
  }

  .venue-name {
    position: absolute;
    left: 7px;
    width: 1200px;
    top: 598px;
    margin: 0;
    text-align: center;
    font-family: "Libre Baskerville", serif;
    font-weight: 700;
    font-size: 38px;
    line-height: 1;
    color: var(--ink-white);
    text-shadow: 3px 4px 5px var(--shadow);
  }
</style>
</head>
<body>
  <main class="namecard">
    <div class="beach-photo" role="img" aria-label="Photograph of a sunny beach with blue sky and golden sand, a woman leaping joyfully while holding a bunch of colourful balloons"></div>
    <h1 class="first-name">Nora</h1>
    <p class="last-name">KESSLER</p>
    <p class="venue-name">The Kiteloft</p>
  </main>
</body>
</html>
```